A specialised Sport management needs a corporate brochure design

We are a specialized company in the management and consultancy of sports events. and need to have a company brochure
We provide the following services;
Event management
Venues management
Production
Ticketing
Consulting
Hospitality
Activity management
Event timing
Branding of event
Event supplies
We need a corporate profile design for our company to showcase the major events that we have covered , with images, information, statistics, surveys, products and services used. We want to highlight our professionalism and execution of the events, experience of the participants, spectators . How we have grown in the past few years and reached the international standards.
Objectives of the work:
To get sponsors and partners for future business and to present Trel-Mark
as not just a sports management company but also a professional sports
events management company.
You can check our website
www.trel-mark.com
Target Market(s)
Sponsors and corporate partners
Industry/Entity Type
Events
Requirements
Must have
- Must Have:
- - Very professional look
- -Some event images,Event information, statistics, surveys, products and services used. We want to highlight our professionalism and execution of the events (Attached)
Nice to have
- Similar momentom of the below design
- http://www.quaviet.it/wp-content/themes/quaviet/pdf/CP-2014-15-V10-Web.pdf

```html
<!DOCTYPE html>
<html lang="en">
<head>
<meta charset="utf-8">
<title>Trel-Mark Corporate Brochure</title>
<link rel="stylesheet" href="https://fonts.googleapis.com/css2?family=Oswald:wght@300;400;600;700&family=Open+Sans:wght@400;600&display=swap">
<style>
  :root {
    --orange: #ef5a24;
    --green: #1c7a3e;
    --ink: #2b2b2b;
    --grey: #6d6d6d;
    --white: #ffffff;
    --badge-sky: #2a8ccf;
    --badge-navy: #23407a;
    --badge-red: #d8232a;
    --shadow: 3px 4px 7px rgba(0,0,0,.28);
  }
  * { margin: 0; padding: 0; box-sizing: border-box; }
  html, body { width: 1200px; height: 1125px; overflow: hidden; background: var(--white); }
  body { position: relative; font-family: "Open Sans", sans-serif; color: var(--ink); }

  .sheet { position: absolute; background: var(--white); box-shadow: var(--shadow); overflow: hidden; }
  .sheet--single { width: 200px; height: 200px; }
  .sheet--spread { width: 402px; height: 200px; }
  .page { position: absolute; top: 0; height: 200px; width: 201px; }
  .page--left { left: 0; }
  .page--right { left: 201px; }
  .photo { position: absolute; }
  .spine { position: absolute; left: 196px; top: 0; width: 10px; height: 200px; background: linear-gradient(90deg, rgba(0,0,0,0), rgba(0,0,0,.12), rgba(255,255,255,.08), rgba(0,0,0,0)); }

  .brand { position: absolute; display: flex; align-items: center; gap: 4px; }
  .brand__dot { width: 11px; height: 11px; border-radius: 50%; background: var(--green); }
  .brand__name { font-family: "Oswald", sans-serif; font-weight: 600; font-size: 12px; letter-spacing: .5px; color: var(--ink); }

  .small { font-size: 3.4px; line-height: 1.45; }
  .label { display: inline-block; font-family: "Oswald", sans-serif; font-weight: 600; font-size: 3.6px; letter-spacing: .2px; padding: 1px 2px; margin-bottom: 2px; }

  /* cover */
  .cover { left: 133px; top: 116px; }
  .cover__photo { inset: 0; background:
      linear-gradient(180deg, #efe7da 0%, #d9cdb9 14%, #b9a58e 26%, #6f8a5c 38%, #a8473d 48%, #d8d2c8 56%, #8a7a6c 68%, #6a5548 80%, #3a2e28 100%); }
  .cover__strip { position: absolute; right: 0; top: 0; width: 9px; height: 200px; background: var(--orange); }
  .cover__brand { left: 84px; top: 16px; }
  .cover__tag { position: absolute; left: 6px; top: 14px; writing-mode: vertical-rl; transform: rotate(180deg); font-size: 3px; color: var(--white); letter-spacing: .5px; }
  .cover__headline { position: absolute; right: 15px; top: 113px; text-align: right; font-family: "Oswald", sans-serif; font-weight: 700; font-size: 17px; line-height: 1.05; color: var(--white); text-shadow: 0 1px 3px rgba(0,0,0,.35); }

  /* about */
  .about { left: 133px; top: 365px; }
  .about__photo { left: 0; top: 0; width: 201px; height: 200px; background:
      linear-gradient(165deg, #e2e0da 0%, #c4beb4 18%, #9a6d5c 34%, #c8b9a6 46%, #5f7a5a 58%, #8c8781 70%, #4a4644 84%, #2a2827 100%); }
  .about__gutter { position: absolute; left: 0; top: 0; width: 26px; height: 200px; background: linear-gradient(90deg, #dcdcdc, #f4f4f4); }
  .about__title { position: absolute; left: 33px; top: 14px; font-family: "Oswald", sans-serif; font-weight: 300; font-size: 15px; color: var(--ink); }
  .about__intro { position: absolute; left: 33px; top: 40px; width: 158px; color: var(--grey); }
  .about__intro p { margin-bottom: 3px; }
  .about__cols { position: absolute; left: 33px; top: 90px; width: 160px; display: flex; gap: 8px; }
  .about__col { flex: 1; }
  .about__col p { margin-bottom: 3px; }
  .label--green { background: var(--green); color: var(--white); }
  .label--orange { background: var(--orange); color: var(--white); }
  .text-green { color: var(--green); }
  .text-orange { color: var(--orange); }

  /* philosophy */
  .philosophy { left: 133px; top: 591px; }
  .philosophy__page { background: var(--orange); color: var(--white); }
  .philosophy__title { position: absolute; left: 12px; top: 12px; font-family: "Oswald", sans-serif; font-weight: 300; font-size: 15px; }
  .philosophy__cols { position: absolute; left: 12px; top: 38px; width: 180px; display: flex; gap: 8px; }
  .philosophy__col { flex: 1; }
  .philosophy__col p { margin-bottom: 4px; }
  .label--white { background: var(--white); color: var(--ink); }
  .philosophy__photo { left: 201px; top: 0; width: 201px; height: 200px; background:
      linear-gradient(180deg, #5f8bc4 0%, #8fb0d6 20%, #c9d3d8 34%, #b4a98f 44%, #d9d4c2 52%, #3d4b6a 62%, #e0d64a 70%, #8e7e6d 80%, #4a4340 100%); }

  /* services */
  .services { left: 133px; top: 819px; }
  .services__photo { inset: 0; background:
      linear-gradient(180deg, #6f93c4 0%, #9db7d4 30%, #c9d4da 48%, #b0a48e 56%, #2f3740 64%, #4d5d6c 76%, #7f96a8 88%, #5b6e7e 100%); }
  .services__list { position: absolute; left: 246px; top: 14px; color: var(--white); font-family: "Oswald", sans-serif; list-style: none; }
  .services__title { font-weight: 600; font-size: 14px; margin-bottom: 4px; }
  .services__item { font-weight: 300; font-size: 10px; line-height: 15.2px; }

  /* history */
  .history { left: 659px; top: 365px; }
  .history__title { position: absolute; left: 12px; top: 11px; font-family: "Oswald", sans-serif; font-weight: 700; font-size: 13.5px; line-height: 1.05; color: var(--orange); }
  .event { position: absolute; display: flex; gap: 4px; width: 160px; }
  .event--right { width: 118px; }
  .event__thumb { width: 30px; height: 26px; flex: none; }
  .event__title { font-family: "Oswald", sans-serif; font-weight: 600; font-size: 3.8px; color: var(--ink); }
  .event__text { color: var(--grey); }
  .event__more { font-family: "Oswald", sans-serif; font-size: 3.4px; color: var(--orange); }
  .history__years { position: absolute; right: 4px; top: 4px; writing-mode: vertical-rl; font-family: "Oswald", sans-serif; font-weight: 300; font-size: 30px; letter-spacing: 1px; color: transparent; -webkit-text-stroke: .6px #b9cfc2; }

  /* partners */
  .partners { left: 659px; top: 591px; }
  .partners__page { background: var(--green); }
  .partners__title { position: absolute; left: 12px; top: 14px; font-family: "Oswald", sans-serif; font-weight: 700; font-size: 13px; color: var(--orange); }
  .partners__badges { position: absolute; left: 13px; top: 56px; display: flex; gap: 7px; }
  .partners__badge { width: 34px; height: 34px; background: var(--white); display: flex; align-items: center; justify-content: center; box-shadow: 1px 1px 3px rgba(0,0,0,.3); }
  .partners__shape { width: 18px; height: 18px; border-radius: 50%; }

  /* back cover */
  .back { left: 659px; top: 819px; }
  .back__fade { position: absolute; left: 0; top: 55px; width: 200px; height: 60px; background: linear-gradient(180deg, #ffffff, #d4d4d4); }
  .back__photo { left: 0; top: 115px; width: 200px; height: 85px; background:
      linear-gradient(180deg, #7d8a90 0%, #4f4a47 25%, #8c7464 45%, #3b3634 65%, #5a6670 82%, #25211f 100%); }
  .back__brand { right: 12px; top: 16px; }
  .back__address { position: absolute; right: 12px; top: 45px; text-align: right; color: var(--grey); font-style: normal; }
  .back__contact { position: absolute; left: 12px; right: 12px; top: 101px; display: flex; justify-content: space-between; font-family: "Oswald", sans-serif; font-size: 7px; color: var(--ink); }
</style>
</head>
<body>

<section class="sheet sheet--single cover">
  <div class="photo cover__photo" role="img" aria-label="Runners in green, red and white team shirts at the start of a road race"></div>
  <div class="cover__strip"></div>
  <span class="cover__tag">PROFILE 2015</span>
  <div class="brand cover__brand"><span class="brand__dot"></span><span class="brand__name">TREL-MARK</span></div>
  <h1 class="cover__headline">LET'S TAKE<br>CARE OF YOUR<br>NEXT SPORTS<br>EVENT!</h1>
</section>

<section class="sheet sheet--spread about">
  <div class="photo about__photo" role="img" aria-label="Fans leaning over a barrier to cheer a kart driver at an indoor karting event"></div>
  <div class="page page--right">
    <div class="about__gutter"></div>
    <h2 class="about__title">ABOUT TREL-MARK</h2>
    <div class="about__intro small">
      <p>Trel-Mark is a lively and specialised company in sports event management and consultancy based in Kuwait.</p>
      <p>Our diverse practice serves clients with a complete management service, to advise and assist in every aspect of your sporting event. At Trel-Mark our aim is to take care of the planning, running and review of local and international sport events, and, most of all, to raise the standards of sports practice.</p>
    </div>
    <div class="about__cols small">
      <div class="about__col text-green">
        <span class="label label--green">TREL-MARK · TOTAL COMMITMENT</span>
        <p>To identify new objectives about the sector, exceed client expectations and raise every event to a higher standard.</p>
        <p>To build firm, long term relationships through our high quality services in sports management and consultancy.</p>
      </div>
      <div class="about__col text-orange">
        <span class="label label--orange">TREL-MARK · FULLY PROVEN</span>
        <p>Trel-Mark is the only specialised organisation in sports management and consultancy in the region.</p>
        <p>Our experts develop every event from the first idea to the final whistle.</p>
      </div>
    </div>
  </div>
</section>

<section class="sheet sheet--spread philosophy">
  <div class="page page--left philosophy__page">
    <h2 class="philosophy__title">PHILOSOPHY</h2>
    <div class="philosophy__cols small">
      <div class="philosophy__col">
        <span class="label label--white">OUR PHILOSOPHY · SPECIALIZATION</span>
        <p>Trel-Mark is the region's leading specialist in the management and consultancy of sports events.</p>
        <p>Established in 2007, our team has grown in size and strength, serving local and international events of every scale with the same care.</p>
        <span class="label label--white">OUR BELIEF · SOCIAL RESPONSIBILITY</span>
        <p>We value people, community and the environment in everything we deliver, and we give back to the sports that made us.</p>
        <p>Each event leaves a legacy: healthier habits, stronger clubs and proud hosts.</p>
      </div>
      <div class="philosophy__col">
        <span class="label label--white">OUR CORE VALUES · REMAIN CONSTANT</span>
        <p>Our core values guide every decision we make, from the first plan to the final delivery.</p>
        <p>Quality, safety, honesty and respect stay at the heart of every project we run.</p>
        <span class="label label--white">OUR TEAM · DEDICATED PROFESSIONALS</span>
        <p>Our staff combines skilled field teams with experienced managers and trusted suppliers.</p>
        <p>Together we plan, build and run events that meet international standards.</p>
      </div>
    </div>
  </div>
  <div class="photo philosophy__photo" role="img" aria-label="Crowd of runners on a seaside road during a city marathon"></div>
  <div class="spine"></div>
</section>

<section class="sheet sheet--spread services">
  <div class="photo services__photo" role="img" aria-label="Triathletes in swim caps entering the sea at sunrise"></div>
  <div class="spine"></div>
  <ul class="services__list">
    <li class="services__title">OUR SERVICES</li>
    <li class="services__item">EVENT MANAGEMENT</li>
    <li class="services__item">VENUES MANAGEMENT</li>
    <li class="services__item">PRODUCTION</li>
    <li class="services__item">TICKETING</li>
    <li class="services__item">CONSULTING</li>
    <li class="services__item">HOSPITALITY</li>
    <li class="services__item">ACTIVITY MANAGEMENT</li>
    <li class="services__item">EVENT TIMING</li>
    <li class="services__item">BRANDING OF EVENT</li>
    <li class="services__item">EVENT SUPPLIES</li>
  </ul>
</section>

<section class="sheet sheet--spread history">
  <h2 class="history__title">FROM SPORTING PAST<br>INTO SPORTING FUTURE<br>WITH OUR PARTNERS</h2>
  <div class="event" style="left:12px; top:104px;">
    <div class="event__thumb" role="img" aria-label="Marathon runners on a city road" style="background:linear-gradient(#d8c9b0,#8a7460,#4e4038);"></div>
    <div class="small"><div class="event__title">City Marathon Weekend</div><div class="event__text">Thousands of runners crossed the city for a full day of racing, with timing, water stations and medical teams along the whole course.</div><div class="event__more">READ MORE</div></div>
  </div>
  <div class="event" style="left:12px; top:136px;">
    <div class="event__thumb" role="img" aria-label="Cyclists on a desert road" style="background:linear-gradient(#e0cfae,#b08f62,#6d563c);"></div>
    <div class="small"><div class="event__title">Desert Cycling Challenge</div><div class="event__text">Riders from twelve nations faced a hard route across open desert roads, supported by our mobile crews and live results.</div><div class="event__more">READ MORE</div></div>
  </div>
  <div class="event" style="left:12px; top:168px;">
    <div class="event__thumb" role="img" aria-label="Triathlon swim start at sea" style="background:linear-gradient(#a9c0d4,#6a7f90,#3a4550);"></div>
    <div class="small"><div class="event__title">Coastal Triathlon Series</div><div class="event__text">A swim, bike and run course staged along the bay front, with full venue build and spectator areas.</div><div class="event__more">READ MORE</div></div>
  </div>
  <div class="event event--right" style="left:226px; top:78px;">
    <div class="event__thumb" role="img" aria-label="Indoor karting race" style="background:linear-gradient(#c4b2a2,#8a5c4c,#4a3e38);"></div>
    <div class="small"><div class="event__title">Indoor Karting Cup</div><div class="event__text">Young drivers competed on a timed track with live results screens and a packed stand.</div><div class="event__more">READ MORE</div></div>
  </div>
  <div class="event event--right" style="left:226px; top:113px;">
    <div class="event__thumb" role="img" aria-label="Students at a sports day" style="background:linear-gradient(#d4bca8,#a0604c,#5a4438);"></div>
    <div class="small"><div class="event__title">Schools Sports Day</div><div class="event__text">Over two thousand students joined games, races and team events across one campus.</div><div class="event__more">READ MORE</div></div>
  </div>
  <div class="event event--right" style="left:226px; top:148px;">
    <div class="event__thumb" role="img" aria-label="Families at a charity run" style="background:linear-gradient(#cfc2b8,#8e7468,#54463e);"></div>
    <div class="small"><div class="event__title">Charity Fun Run</div><div class="event__text">Families walked and ran together to support local health programmes by the sea.</div><div class="event__more">READ MORE</div></div>
  </div>
  <div class="history__years">1990–2015</div>
</section>

<section class="sheet sheet--spread partners">
  <div class="page page--left partners__page">
    <h2 class="partners__title">PARTNERS PAGE</h2>
    <div class="partners__badges">
      <span class="partners__badge"><span class="partners__shape" style="background:var(--badge-sky);"></span></span>
      <span class="partners__badge"><span class="partners__shape" style="background:var(--badge-navy);"></span></span>
      <span class="partners__badge"><span class="partners__shape" style="background:var(--badge-red);"></span></span>
      <span class="partners__badge"><span class="partners__shape" style="background:var(--badge-navy); border-radius:0;"></span></span>
    </div>
  </div>
</section>

<section class="sheet sheet--single back">
  <div class="back__fade"></div>
  <div class="photo back__photo" role="img" aria-label="Swimmers wading into the water at a triathlon start"></div>
  <div class="brand back__brand"><span class="brand__dot"></span><span class="brand__name">TREL-MARK</span></div>
  <address class="back__address small">
    Block 4, Street 12<br>Sharq, Kuwait City<br>Tel +965 2000 1122<br>info@trel-mark.com
  </address>
  <div class="back__contact"><span>WWW.TREL-MARK.COM</span><span>+965 2 000 11 22</span></div>
</section>

</body>
</html>
```